law firm business cards

I need a business card using my existing logo. Two sided is best because there is a lot of information that needs to go on the card. Use the same general color scheme as logo, but I need one set with the blue background of my website (www.halvorsenlawgrp.com), and one set with white background (to see which one I like best).

Information that must be on there:
Trevor J. Halvorsen
Board Certified Civil Trial Specialist
738 Brinkley Ave., Suite 640
Raleigh, NC 27601

T 919-555-0143
F 919-555-0176

www.halvorsenlawgrp.com
trevor@halvorsenlawgrp.com

Personal Injury | Criminal Law (to separate the two, pls use a bullet point or pipeline symbol "|"

If there is a way to work in the CPRS logo (maybe at the bottom somewhere), put it in, but don't let it detract from the main logo too much.

Also, if there is a way to work it in, put in somewhere: Former Insurance Company Attorney | Former Criminal Prosecutor (to separate the two, pls use a bullet point or pipeline symbol "|"

```html
<!DOCTYPE html>
<html lang="en">
<head>
<meta charset="utf-8">
<title>Halvorsen Law – Business Cards</title>
<link rel="stylesheet" href="https://fonts.googleapis.com/css2?family=Cinzel:wght@500;600&family=Open+Sans:wght@400;600&display=swap">
<style>
  :root {
    --navy: #1c3566;
    --navy-deep: #15294f;
    --sky: #4a86c8;
    --red: #e0223f;
    --white: #ffffff;
    --grey: #8a8d93;
    --backdrop: #e6e4e0;
  }
  * { box-sizing: border-box; margin: 0; padding: 0; }
  html, body { width: 1200px; height: 469px; overflow: hidden; }
  body { background: var(--backdrop); position: relative; font-family: "Open Sans", Arial, sans-serif; }

  .card {
    position: absolute;
    top: 102px;
    width: 470px;
    height: 264px;
    box-shadow: 0 3px 8px rgba(0,0,0,0.25);
  }
  .card--front { left: 106px; background: var(--navy); color: var(--white); }
  .card--back { left: 606px; background: var(--white); color: var(--navy); }

  .firm-name {
    position: absolute;
    left: 0; right: 0;
    display: flex;
    justify-content: center;
    align-items: center;
    gap: 12px;
    font-family: "Cinzel", Georgia, serif;
    font-weight: 600;
    letter-spacing: 0.5px;
    white-space: nowrap;
  }
  .firm-name__mark { width: 30px; height: 30px; border-radius: 50%; }
  .card--front .firm-name { top: 42px; font-size: 38px; color: var(--white); }
  .card--front .firm-name__mark { background: var(--white); }
  .card--back .firm-name { top: 24px; font-size: 30px; color: var(--navy); }
  .card--back .firm-name__mark { width: 24px; height: 24px; background: var(--navy); }

  .attorney-name {
    position: absolute;
    top: 140px; left: 0; right: 0;
    text-align: center;
    font-family: "Cinzel", Georgia, serif;
    font-weight: 500;
    font-size: 19px;
    letter-spacing: 1px;
  }

  .details {
    position: absolute;
    top: 204px;
    font-size: 11.5px;
    line-height: 14px;
  }
  .details--address { left: 30px; }
  .details--contact { left: 264px; }
  .details__label { color: var(--red); }
  .details__web { font-weight: 600; letter-spacing: 0.6px; margin-top: 1px; }
  .details-divider {
    position: absolute;
    left: 236px; top: 204px;
    width: 1px; height: 44px;
    background: var(--red);
  }

  .membership-seal {
    position: absolute;
    left: 202px; top: 82px;
      width: 66px; height: 66px;
  }

  .practice-areas {
    position: absolute;
    top: 180px; left: 0; right: 0;
    text-align: center;
    font-family: "Cinzel", Georgia, serif;
    font-weight: 600;
    font-size: 14px;
    letter-spacing: 0.5px;
  }
  .sep { color: var(--red); margin: 0 8px; font-family: "Open Sans", Arial, sans-serif; font-weight: 400; }

  .web-pill {
    position: absolute;
    top: 206px; left: 86px;
    width: 288px; height: 21px;
    border-radius: 11px;
    background: var(--navy);
    color: var(--white);
    font-size: 12px;
    font-weight: 600;
    letter-spacing: 2.4px;
    line-height: 21px;
    text-align: center;
  }

  .background-roles {
    position: absolute;
    top: 234px; left: 0; right: 0;
    text-align: center;
    font-size: 11px;
    letter-spacing: 0.6px;
    color: var(--grey);
  }
</style>
</head>
<body>

  <section class="card card--front" aria-label="Business card, blue front">
    <div class="firm-name"><span class="firm-name__mark"></span>HALVORSEN LAW</div>
    <div class="attorney-name">TREVOR J. HALVORSEN</div>

    <div class="details details--address">
      <div>Board Certified Civil Trial Specialist</div>
      <div>738 Brinkley Ave., Suite 640</div>
      <div>Raleigh, NC 27601</div>
    </div>
    <div class="details-divider"></div>
    <div class="details details--contact">
      <div><span class="details__label">T:</span> 919-555-0143,&nbsp; <span class="details__label">F:</span> 919-555-0176</div>
      <div><span class="details__label">E:</span> trevor@halvorsenlawgrp.com</div>
      <div class="details__web">www.halvorsenlawgrp.com</div>
    </div>
  </section>

  <section class="card card--back" aria-label="Business card, white back">
    <div class="firm-name"><span class="firm-name__mark"></span>HALVORSEN LAW</div>

    <svg class="membership-seal" viewBox="0 0 66 66" role="img" aria-label="CPRS membership badge">
      <circle cx="33" cy="33" r="31" fill="none" stroke="var(--navy)" stroke-width="1.5"/>
      <circle cx="33" cy="33" r="22" fill="none" stroke="var(--navy)" stroke-width="1"/>
    </svg>

    <div class="practice-areas">PERSONAL INJURY<span class="sep">|</span>CRIMINAL LAW</div>
    <div class="web-pill">www.halvorsenlawgrp.com</div>
    <div class="background-roles">Former Insurance Company Attorney<span class="sep">|</span>Former Criminal Prosecutor</div>
  </section>

</body>
</html>
```